Bref créative
Cool Cards for Engineering and design business
Borealis Drafting and Systems Inc.
Professional
Derek Wolfe
President
#22 - 3407 6th street
Nisku, Ab
T4R 2K9
derek.wolfe@borealisdraftsys.ca
www.borealisdraftsys.ca
Please use clear standard font. We can try some with the logo font. I want the card to be modern POP and stand out.
Please put a QR code on the back with the contact info. I want this designed so it is optional and can be printed as a single card too.

```html
<!DOCTYPE html>
<html lang="en">
<head>
<meta charset="utf-8">
<title>Borealis Drafting and Systems Inc. – Business Card</title>
<link href="https://fonts.googleapis.com/css2?family=Exo+2:wght@400;600;800&family=Montserrat:wght@400;600&display=swap" rel="stylesheet">
<style>
  :root {
    --bg: #ecebe8;
    --charcoal: #353535;
    --charcoal-deep: #2b2b2b;
    --green: #3cc63a;
    --green-dark: #2a9e2a;
    --white: #ffffff;
    --grey-text: #cfcfcf;
  }
  * { box-sizing: border-box; margin: 0; padding: 0; }
  html, body { width: 1200px; height: 991px; overflow: hidden; }
  body {
    background: var(--bg);
    font-family: "Montserrat", sans-serif;
    display: flex; flex-direction: column; align-items: center; justify-content: center;
    gap: 56px;
  }
  .card {
    position: relative;
    width: 700px; height: 400px;
    overflow: hidden;
    box-shadow: 0 6px 18px rgba(0,0,0,.18);
  }
  /* Back */
  .card-back {
    background: var(--charcoal);
    display: flex; flex-direction: column; align-items: center; justify-content: center;
    gap: 34px;
  }
  .brand { display: flex; align-items: center; gap: 18px; }
  .brand-dot {
    width: 58px; height: 58px; border-radius: 50%;
    background: var(--green);
    flex: none;
  }
  .brand-name {
    font-family: "Exo 2", sans-serif; font-weight: 800;
    text-transform: uppercase; line-height: 1.05;
    font-size: 30px; color: var(--white);
  }
  .brand-name small { display: block; font-size: 14px; letter-spacing: 2px; }
  .web-line {
    display: flex; align-items: center; gap: 14px;
    color: var(--green); font-size: 14px; letter-spacing: 5px; text-transform: uppercase;
  }
  .web-line::before, .web-line::after {
    content: ""; width: 40px; height: 2px; background: var(--green);
  }
  /* Front */
  .card-front { background: var(--white); }
  .front-shape { position: absolute; inset: 0; }
  .card-front .brand { position: absolute; left: 190px; top: 62px; }
  .card-front .brand-name { color: var(--charcoal); }
  .identity {
    position: absolute; left: 140px; top: 258px; width: 200px; text-align: right;
    color: var(--white);
  }
  .identity .person { font-family: "Exo 2", sans-serif; font-weight: 600; font-size: 17px; letter-spacing: 1px; text-transform: uppercase; }
  .identity .role { color: var(--green); font-size: 11px; letter-spacing: 2px; text-transform: uppercase; margin-top: 2px; }
  .identity .address { color: var(--grey-text); font-size: 11px; line-height: 1.6; margin-top: 14px; }
  .divider {
    position: absolute; left: 362px; top: 256px; width: 1px; height: 112px;
    background: var(--green);
  }
  .contacts {
    position: absolute; left: 384px; top: 258px; list-style: none;
    color: var(--grey-text); font-size: 11px;
  }
  .contacts li { display: flex; align-items: center; gap: 9px; height: 21px; }
  .contacts svg { width: 13px; height: 13px; fill: var(--green); flex: none; }
</style>
</head>
<body>

  <section class="card card-back" aria-label="Card back">
    <div class="brand">
      <span class="brand-dot"></span>
      <p class="brand-name">Borealis<small>Drafting and Systems Inc.</small></p>
    </div>
    <p class="web-line">www.borealisdraftsys.ca</p>
  </section>

  <section class="card card-front" aria-label="Card front">
    <svg class="front-shape" viewBox="0 0 700 400" preserveAspectRatio="none" aria-hidden="true">
      <path d="M0 228 C 220 215, 470 175, 700 128 L700 400 L0 400 Z" fill="var(--charcoal)"/>
      <path d="M0 214 C 230 205, 470 168, 700 112 L700 128 C 470 175, 220 215, 0 228 Z" fill="var(--green)"/>
      <path d="M120 200 C 330 190, 520 150, 700 92 L700 98 C 520 160, 330 198, 120 200 Z" fill="var(--green-dark)"/>
    </svg>

    <div class="brand">
      <span class="brand-dot"></span>
      <p class="brand-name">Borealis<small>Drafting and Systems Inc.</small></p>
    </div>

    <div class="identity">
      <p class="person">Derek Wolfe</p>
      <p class="role">President</p>
      <p class="address">#22 - 3407 6th street<br>Nisku, Ab<br>T4R 2K9</p>
    </div>
    <span class="divider"></span>

    <ul class="contacts">
      <li><svg viewBox="0 0 16 16"><path d="M3 1h3l1.5 4-2 1.2a9 9 0 0 0 4.3 4.3L11 8.5l4 1.5v3a2 2 0 0 1-2 2A12 12 0 0 1 1 3a2 2 0 0 1 2-2z"/></svg>780-555-0142</li>
      <li><svg viewBox="0 0 16 16"><path d="M3 1h3l1.5 4-2 1.2a9 9 0 0 0 4.3 4.3L11 8.5l4 1.5v3a2 2 0 0 1-2 2A12 12 0 0 1 1 3a2 2 0 0 1 2-2z"/></svg>780-555-0187</li>
      <li><svg viewBox="0 0 16 16"><rect x="4" y="1" width="8" height="14" rx="1.5"/></svg>780-555-0163</li>
      <li><svg viewBox="0 0 16 16"><path d="M1 3h14v10H1z M1 3l7 6 7-6" stroke="#353535" stroke-width="1"/></svg>derek.wolfe@borealisdraftsys.ca</li>
      <li><svg viewBox="0 0 16 16"><circle cx="8" cy="8" r="7"/></svg>www.borealisdraftsys.ca</li>
    </ul>
  </section>

</body>
</html>
```